Online Book Sale Postcard Design

I need a postcard design to announce the online sale of my paperback book listed on Trovaly.com and Pagebrook.com. My book is about Christmas and belief in God told in short stories, poems, and prayer to help individuals, children, and families celebrate Christmas.
I live in Houston, TX with my retired parents and younger sister in our neighborhood that has a lot of retired citizens and neighbors. The book is a tribute to the neighborhood which is the source of inspiration for the poem which has the same title as the book "Humming Bells, Drifting Snow." I wrote that poem in 2001 after a car tour of the neighborhood in December of 2000.
This is my first book that I've written and is listed on Trovaly.com and PageBrook.com. I have a high resolution cover jpeg upload that I would like to use on the front (full color) of the postcard. The basic information showing when it's for sale and where it can be bought is what I need printed on the postcard. I have marketing copy that can be used, also. I want the postcard to convey joy and cheer to communicate the mood of the season as well as of the book, "Humming Bells, Drifting Snow."
Target Market(s)
Females aged 35+, influenced by husbands and young children, teenagers, and young adults.
Industry/Entity Type
Marketing
Requirements
Nice to have
- I trust your creative judgment. Something that makes homeowners want to keep the postcard for reference and as a reminder to buy for themselves and/or give as a gift.
Should not have
- Don't crowd the postcard with too much information. Specifics is all that's needed. I trust your judgment.

```html
<!DOCTYPE html>
<html lang="en">
<head>
<meta charset="utf-8">
<title>Humming Bells, Drifting Snow – Postcard</title>
<link href="https://fonts.googleapis.com/css2?family=Roboto+Condensed:wght@300;400&display=swap" rel="stylesheet">
<style>
  :root {
    --paper: #ffffff;
    --gold: #b39a1c;
    --gold-line: #c9a83a;
    --ribbon-light: #f7e6b0;
    --ribbon-mid: #e3bb55;
    --maroon: #8a1c2b;
    --red: #b3121c;
    --red-dark: #8c0b12;
    --bauble-red: #a8162a;
    --bauble-pale: #f7e3e5;
    --grey: #8a9499;
  }
  html, body { margin: 0; padding: 0; overflow: hidden; background: var(--paper); }
  .postcard {
    position: relative; width: 1200px; height: 923px; overflow: hidden;
    background: var(--paper);
    font-family: "Roboto Condensed", "Arial Narrow", sans-serif;
  }
  .postcard > * { position: absolute; margin: 0; }

  .ribbon-art {
    left: 0; top: 0; width: 572px; height: 200px;
    background: linear-gradient(180deg, var(--paper) 0%, var(--ribbon-light) 18%, var(--ribbon-mid) 45%, var(--ribbon-light) 75%, var(--paper) 100%);
  }
  .ornament-art {
    left: 0; top: 772px; width: 180px; height: 151px;
    background: linear-gradient(135deg, var(--bauble-pale) 0%, var(--bauble-red) 55%, #7e0f1f 100%);
  }
  .divider { left: 572px; top: 0; width: 6px; height: 742px; background: var(--maroon); }

  .greeting {
    left: 0; top: 206px; width: 594px; text-align: center;
    color: var(--gold); font-size: 23px; line-height: 30px; font-weight: 400;
    letter-spacing: 0.9px;
  }
  .blurb {
    left: 0; top: 306px; width: 602px; text-align: center;
    color: var(--maroon); font-size: 27.5px; line-height: 43px; font-weight: 300;
  }
  .title-credit {
    left: 36px; top: 547px; color: var(--gold); font-size: 31px; line-height: 38px; font-weight: 300;
  }
  .author-name {
    left: 36px; top: 639px; color: var(--maroon); font-size: 31px; line-height: 40px; font-weight: 400;
  }
  .author-address {
    left: 36px; top: 678px; color: var(--maroon); font-size: 27px; line-height: 37px; font-weight: 300;
  }
  .availability {
    left: 278px; top: 543px; width: 267px; height: 125px; text-align: center;
    background: linear-gradient(180deg, var(--red) 0%, var(--red-dark) 100%);
    box-shadow: 0 8px 12px rgba(0,0,0,0.22);
    color: #fff; font-weight: 400;
  }
  .availability .lead { display: block; font-size: 24px; line-height: 26px; margin-top: 8px; }
  .availability .store { display: block; font-size: 34px; line-height: 40px; }

  .author-photo {
    left: 629px; top: 18px; width: 192px; height: 192px;
    background: linear-gradient(160deg, #5b7dc4 0%, #2f4f9a 55%, #1d1d24 100%);
    border: 3px solid #fff; box-shadow: 0 0 4px rgba(0,0,0,0.35);
  }
  .photo-caption {
    left: 626px; top: 220px; width: 200px; text-align: center;
    color: var(--maroon); font-size: 27px; line-height: 36px; font-weight: 300;
  }
  .postage-box {
    left: 975px; top: 75px; width: 136px; height: 136px;
    border: 2px solid var(--gold-line);
    display: flex; align-items: center; justify-content: center; text-align: center;
    color: var(--grey); font-size: 23px; line-height: 29px; font-family: Arial, sans-serif;
  }
  .address-lines { left: 695px; top: 440px; width: 406px; height: 218px; }
</style>
</head>
<body>
<main class="postcard">
  <div class="ribbon-art" role="img" aria-label="Gold satin ribbon bow with a red Christmas bauble"></div>
  <div class="divider"></div>

  <p class="greeting">“Christmas Greetings to You, Dear Friends!<br>In the Spirit of Love, come with your cares.<br>In the Spirit of Thanksgiving, come with your prayers.”</p>

  <p class="blurb">“Humming Bells, Drifting Snow”<br>beckons you to embrace the wonder of Christmas<br>through a cheerful collection of warm words,<br>delightful rhymes, and inspiring reflections that<br>reconnect you to the childlike joy of the season.</p>

  <p class="title-credit">“Humming Bells,<br>Drifting Snow” by</p>
  <p class="author-name">Lorna B. Whitfield</p>
  <p class="author-address">Author (and longtime Maplecrest resident)<br>4120 Larkspur Lane, Houston, TX 77031</p>

  <div class="availability">
    <span class="lead">Now Available on</span>
    <span class="store">Trovaly.com &amp;</span>
    <span class="store">PageBrook.com</span>
  </div>

  <div class="ornament-art" role="img" aria-label="Red Christmas baubles with gold trim and small gift boxes"></div>

  <div class="author-photo" role="img" aria-label="Portrait photo of the author"></div>
  <p class="photo-caption">Lorna B. Whitfield<br>Author</p>

  <div class="postage-box">Postage<br>Area</div>

  <svg class="address-lines" viewBox="0 0 406 218" aria-hidden="true">
    <g stroke="#c9a83a" stroke-width="2">
      <line x1="0" y1="1" x2="406" y2="1"/>
      <line x1="0" y1="72" x2="406" y2="72"/>
      <line x1="0" y1="143" x2="406" y2="143"/>
      <line x1="0" y1="214" x2="406" y2="214"/>
    </g>
  </svg>
</main>
</body>
</html>
```